Velorine Jewellery Display Card

We are a jewellery manufacturer and need artwork for an A4 size strut card to advertise our new "Crescent Loop Pendant "
In the attached files is a picture of the new pendant and artwork for our trademark "Velorine"
We also need to include the phrase " an expression of love "
as part of the artwork.
The background colour should be predominately white

Target Market(s)

This product has been designed as a gift for Mothers as it has their children names
engraved on the pendant

Industry/Entity Type

Manufacturer

Font styles to use
Serif
Script

Colors
ffffff

Requirements
Must have
• Artwork should be simple and elegant , the predominant look in Australian jewellery stores which is where these display cards will be is white, bright and elegant

```html
<!DOCTYPE html>
<html lang="en">
<head>
<meta charset="utf-8">
<title>Velorine – Crescent Loop Pendant Display Card</title>
<link rel="stylesheet" href="https://fonts.googleapis.com/css2?family=Comfortaa:wght@300;400&family=Great+Vibes&display=swap">
<style>
  :root {
    --backdrop: #f2f2f2;
    --card-white: #ffffff;
    --magenta: #d1359b;
    --pink-light: #e47fbf;
    --title-pink: #e22d9f;
    --brand-tint: #f3cfe6;
    --script-ink: #222222;
    --silver-light: #f4f4f6;
    --silver-mid: #c9cbd0;
    --silver-dark: #8e9096;
  }
  * { margin: 0; padding: 0; box-sizing: border-box; }
  html, body {
    width: 1200px;
    height: 604px;
    overflow: hidden;
    background: var(--backdrop);
  }
  .stage {
    position: relative;
    width: 1200px;
    height: 604px;
  }
  .display-card {
    position: absolute;
    left: 398px;
    top: 18px;
    width: 404px;
    height: 568px;
    background: var(--card-white);
    overflow: hidden;
    box-shadow: 0 2px 10px rgba(0,0,0,0.08);
  }
  .card-bands {
    position: absolute;
    inset: 0;
    width: 404px;
    height: 568px;
  }
  .headline {
    position: absolute;
    top: 38px;
    left: 0;
    width: 100%;
    text-align: center;
    font-family: "Comfortaa", sans-serif;
    font-weight: 300;
    color: var(--title-pink);
    font-size: 28px;
    line-height: 40px;
    letter-spacing: 0.5px;
    text-shadow: 0 0 6px rgba(226, 45, 159, 0.25);
  }
  .headline-line { display: block; }
  .headline-accent {
    display: inline-block;
    width: 42px;
    height: 16px;
    margin-left: 6px;
    vertical-align: 2px;
    border-radius: 8px;
    background: var(--title-pink);
    opacity: 0.8;
  }
  .pendant-photo {
    position: absolute;
    left: 96px;
    top: 148px;
    width: 212px;
    height: 238px;
    border-radius: 50% 50% 48% 48% / 44% 44% 56% 56%;
    background: radial-gradient(circle at 45% 40%, var(--silver-light) 0%, var(--silver-mid) 60%, var(--silver-dark) 100%);
  }
  .product-name {
    position: absolute;
    top: 414px;
    left: 0;
    width: 100%;
    text-align: center;
    font-family: "Great Vibes", cursive;
    font-size: 17px;
    color: var(--script-ink);
  }
  .brand-name {
    position: absolute;
    right: 36px;
    top: 512px;
    font-family: "Comfortaa", sans-serif;
    font-weight: 400;
    font-size: 27px;
    letter-spacing: 0.5px;
    color: var(--brand-tint);
  }
</style>
</head>
<body>
<main class="stage">
  <article class="display-card">
    <svg class="card-bands" viewBox="0 0 404 568" aria-hidden="true">
      <polygon points="0,0 404,0 404,18 202,9 0,18" fill="var(--pink-light)"/>
      <polygon points="0,0 404,0 404,6 202,3 0,6" fill="var(--magenta)"/>
      <polygon points="0,462 404,440 404,568 0,568" fill="var(--pink-light)"/>
      <polygon points="0,494 404,446 404,568 0,568" fill="var(--magenta)"/>
    </svg>

    <h1 class="headline">
      <span class="headline-line">Expression Of Love</span>
      <span class="headline-line">For Mother<span class="headline-accent" role="img" aria-label="Decorative cluster of small hearts"></span></span>
    </h1>

    <div class="pendant-photo" role="img" aria-label="Photograph of the silver Crescent Loop Pendant with engraved children's names"></div>

    <p class="product-name">Crescent Loop Pendant</p>

    <p class="brand-name">VELORINE</p>
  </article>
</main>
</body>
</html>
```